We were billed for this because the project timed out. Please give me another designed to open this back up. I was not happy with the last designs (that I was charged for).
we are also using the logo with Keeping Every Pool Clear and Balanced
Also want to utilize Where Healthy Water is our Commitment.

Contact Information for Business Card

Marlowe Crest Group Inc

```html
<!DOCTYPE html>
<html lang="en">
<head>
<meta charset="utf-8">
<title>Marlowe Crest Group – Business Card</title>
<link rel="stylesheet" href="https://fonts.googleapis.com/css2?family=Orbitron:wght@800&family=Montserrat:wght@400;500;700&display=swap">
<style>
  :root {
    --backdrop: #141414;
    --card: #262626;
    --card-edge: #333333;
    --ink: #ffffff;
    --ink-soft: #e6e6e6;
    --blue: #1e78c8;
    --blue-light: #4aa8e2;
  }
  * { box-sizing: border-box; margin: 0; padding: 0; }
  html, body { width: 1200px; height: 900px; overflow: hidden; background: var(--backdrop); }
  .stage { position: relative; width: 1200px; height: 900px; }
  .card {
    position: absolute; left: 280px; width: 640px; height: 366px; overflow: hidden;
    background: linear-gradient(135deg, #1f1f1f 0%, var(--card) 60%, var(--card-edge) 100%);
    box-shadow: 0 12px 30px rgba(0,0,0,.6);
  }
  .card--front { top: 70px; }
  .card--back { top: 464px; }

  .wordmark { font-family: "Orbitron", sans-serif; font-weight: 800; color: var(--ink); letter-spacing: .04em; white-space: nowrap; }
  .tagline { font-family: "Montserrat", sans-serif; color: var(--ink-soft); letter-spacing: .2em; text-transform: uppercase; white-space: nowrap; }

  .front-brand { position: absolute; left: 40px; right: 40px; top: 140px; text-align: center; }
  .front-brand .mark-row { display: flex; align-items: center; justify-content: center; gap: 12px; }
  .front-brand .square { width: 20px; height: 20px; background: var(--blue-light); flex: none; }
  .front-brand .wordmark { font-size: 26px; }
  .front-brand .tagline { font-size: 12px; margin-top: 12px; }

  .back-brand { position: absolute; left: 42px; top: 36px; }
  .back-brand .wordmark { font-size: 16px; }
  .back-brand .tagline { font-size: 7px; letter-spacing: .18em; margin-top: 5px; }

  .person { position: absolute; left: 42px; top: 104px; padding-left: 20px; }
  .person::before { content: ""; position: absolute; left: 0; top: 2px; width: 8px; height: 40px; background: var(--blue); border-radius: 2px; }
  .person .name { font-family: "Montserrat", sans-serif; font-weight: 700; font-size: 26px; color: var(--blue); letter-spacing: .06em; text-transform: uppercase; line-height: 1; white-space: nowrap; }
  .person .role { font-family: "Montserrat", sans-serif; font-size: 13px; color: var(--ink); letter-spacing: .08em; text-transform: uppercase; margin-top: 6px; }

  .address { position: absolute; left: 46px; top: 180px; font-family: "Montserrat", sans-serif; font-size: 14px; color: var(--ink); line-height: 1.45; letter-spacing: .02em; }

  .contacts { position: absolute; left: 46px; top: 248px; list-style: none; font-family: "Montserrat", sans-serif; font-size: 14px; color: var(--ink); }
  .contacts li { display: flex; align-items: center; gap: 10px; height: 26px; }
  .contacts svg { width: 14px; height: 14px; fill: var(--blue); flex: none; }

  .back-name { position: absolute; right: 46px; top: 188px; text-align: right; font-family: "Orbitron", sans-serif; font-weight: 800; color: var(--blue-light); font-size: 30px; line-height: 1.2; letter-spacing: .04em; }
</style>
</head>
<body>
<main class="stage">
  <section class="card card--front">
    <div class="front-brand">
      <div class="mark-row">
        <span class="square"></span>
        <span class="wordmark">MARLOWE CREST GROUP</span>
      </div>
      <p class="tagline">Keeping Every Pool Clear and Balanced</p>
    </div>
  </section>

  <section class="card card--back">
    <div class="back-brand">
      <p class="wordmark">MARLOWE CREST GROUP</p>
      <p class="tagline">Keeping Every Pool Clear and Balanced</p>
    </div>

    <div class="person">
      <p class="name">Dana Whitfield</p>
      <p class="role">Manager</p>
    </div>

    <p class="address">482 Lakeview Terrace<br>Fairmont, MN 56031</p>

    <ul class="contacts">
      <li><svg viewBox="0 0 24 24"><path d="M6.6 10.8a15.1 15.1 0 0 0 6.6 6.6l2.2-2.2a1 1 0 0 1 1-.25 11.4 11.4 0 0 0 3.6.57 1 1 0 0 1 1 1V20a1 1 0 0 1-1 1A17 17 0 0 1 3 4a1 1 0 0 1 1-1h3.5a1 1 0 0 1 1 1c0 1.25.2 2.45.57 3.6a1 1 0 0 1-.25 1z"/></svg>(507)555-0142</li>
      <li><svg viewBox="0 0 24 24"><path d="M2 5h20v14H2z M2 5l10 8 10-8" /></svg>hello@marlowecrest.com</li>
      <li><svg viewBox="0 0 24 24"><path d="M12 2a10 10 0 1 0 0 20 10 10 0 0 0 0-20zm6.9 6h-3a15.6 15.6 0 0 0-1.3-3.9A8 8 0 0 1 18.9 8zM12 4c.9 1.2 1.6 2.5 2 4h-4c.4-1.5 1.1-2.8 2-4zM4.3 14a8 8 0 0 1 0-4h3.4a16 16 0 0 0 0 4zm.8 2h3a15.6 15.6 0 0 0 1.3 3.9A8 8 0 0 1 5.1 16zm3-8h-3a8 8 0 0 1 4.3-3.9A15.6 15.6 0 0 0 8.1 8zM12 20c-.9-1.2-1.6-2.5-2-4h4c-.4 1.5-1.1 2.8-2 4zm2.3-6H9.7a14.7 14.7 0 0 1 0-4h4.6a14.7 14.7 0 0 1 0 4zm.3 5.9a15.6 15.6 0 0 0 1.3-3.9h3a8 8 0 0 1-4.3 3.9zM16.3 14a16 16 0 0 0 0-4h3.4a8 8 0 0 1 0 4z"/></svg>www.marlowecrest.com</li>
    </ul>

    <p class="back-name">MARLOWE<br>CREST</p>
  </section>
</main>
</body>
</html>
```